Recommend a friend FLYER - Brisk Window Cleaning

Window cleaning company with focus on quality of service and professionalism. Friendly, relaxed tone, and simple clear communications.

Target Market(s)

Homeowners with moderate income

Industry/Entity Type

Window Cleaning

Font styles to use
Serif
Decorative

Colors
33a6d7
fbee3d
faa54b
d3d3d3

```html
<!DOCTYPE html>
<html lang="en">
<head>
<meta charset="utf-8">
<title>Brisk Window Cleaning – Refer a Friend</title>
<link rel="stylesheet" href="https://fonts.googleapis.com/css2?family=Montserrat:ital,wght@0,400;0,600;0,700;0,800;1,400&family=Open+Sans:wght@400;600&display=swap">
<style>
:root{
  --sky:#0ea2dd;
  --band:#33a6d7;
  --band-edge:#d3d3d3;
  --navy:#2a4c9c;
  --ink:#1c1c1c;
  --white:#ffffff;
  --pale:#dcebf6;
  --sun:#fbee3d;
  --amber:#faa54b;
}
*{margin:0;padding:0;box-sizing:border-box}
html,body{width:1171px;height:1200px;overflow:hidden}
body{background:var(--sky);position:relative;font-family:"Montserrat",sans-serif}

.poster{position:absolute;left:35px;top:40px;width:1109px;height:738px;overflow:hidden;background:var(--white);box-shadow:6px 8px 16px rgba(0,0,0,.35)}
.poster-photo{position:absolute;inset:0;background:linear-gradient(180deg,#f1efe8 0%,#dfe7dc 30%,#b9c8b0 48%,#ece9e2 70%,#f4f1ec 100%)}
.poster-shapes{position:absolute;inset:0}
.wordmark{position:absolute;left:52px;top:228px;color:var(--navy)}
.wordmark-name{display:flex;align-items:center;gap:14px;font-weight:800;font-size:104px;line-height:1;letter-spacing:-2px}
.wordmark-square{width:62px;height:62px;background:var(--band)}
.wordmark-tag{font-weight:700;font-size:27px;margin:6px 0 0 70px}
.band-text{position:absolute;color:var(--white);font-style:italic;font-weight:400;font-size:44px;line-height:60px;letter-spacing:-.5px}
.band-text.one{left:58px;top:428px}
.band-text.two{left:412px;top:598px}

.referral-front{position:absolute;left:35px;top:801px;width:521px;height:376px;display:flex;box-shadow:6px 8px 16px rgba(0,0,0,.35)}
.card-front{position:relative;flex:1;border-right:1px solid #333;background:linear-gradient(180deg,#d4e4ef 0%,#b7cfe0 35%,#c9dbe8 70%,#dbe7f0 100%);text-align:center;color:var(--ink)}
.card-front:last-child{border-right:none}
.mascot{position:absolute;left:58px;top:22px;width:56px;height:62px;border-radius:50% 50% 45% 45%;background:radial-gradient(circle at 50% 40%,#6cc2ee,#2d93cf)}
.pill{position:absolute;left:36px;top:86px;width:102px;height:40px;border-radius:20px;background:#5bb4e6;color:var(--white);font-weight:700;font-size:12px;line-height:15px;padding-top:5px}
.front-brand{position:absolute;left:0;right:0;top:124px;display:flex;justify-content:center;align-items:center;gap:5px;color:var(--navy);font-weight:800;font-size:32px;line-height:1}
.front-brand span.sq{width:18px;height:18px;background:var(--band)}
.front-tag{position:absolute;left:0;right:0;top:158px;font-size:8px;font-weight:600;color:var(--navy)}
.front-get{position:absolute;left:0;right:0;top:180px;font-weight:600;font-size:15px}
.front-amount{position:absolute;left:0;right:0;top:202px;font-weight:800;font-size:54px;line-height:1}
.front-voucher{position:absolute;left:0;right:0;top:258px;font-weight:800;font-size:21px}
.front-thanks{position:absolute;left:0;right:0;top:292px;font-family:"Open Sans",sans-serif;font-size:15px;line-height:16px}
.front-thanks b{font-weight:600}
.front-foot{position:absolute;left:0;right:0;bottom:0;height:30px;background:var(--white);font-family:"Open Sans",sans-serif;font-size:8.5px;line-height:30px}

.referral-back{position:absolute;left:609px;top:801px;width:535px;height:376px;display:flex;background:var(--white);box-shadow:6px 8px 16px rgba(0,0,0,.35)}
.card-back{position:relative;flex:1;border-right:1px solid #333;background:linear-gradient(180deg,#d3e5f3 0%,#e9f2f9 55%,#f8fbfd 100%);padding:0 14px;font-family:"Open Sans",sans-serif;color:var(--ink)}
.card-back:last-child{border-right:none}
.hang-hole{position:absolute;left:50%;top:-16px;width:34px;height:34px;margin-left:-17px;border-radius:50%;background:var(--white)}
.back-brand{margin-top:28px;display:flex;justify-content:center;align-items:center;gap:3px;font-family:"Montserrat",sans-serif;font-weight:800;font-size:19px;color:#333;line-height:1}
.back-brand .sq{width:10px;height:10px;background:#555}
.back-title{text-align:center;font-family:"Montserrat",sans-serif;font-weight:700;font-size:13px;margin-top:2px}
.field{font-size:7.5px;display:flex;align-items:flex-end;height:18px}
.field::after{content:"";flex:1;border-bottom:1px solid #333;margin-left:2px}
.field.gap{margin-top:14px}
.field.line{margin-top:16px}
.sub{text-align:center;font-size:7.5px;margin-top:8px}
.terms{font-size:7.3px;line-height:12.5px;margin-top:4px}
</style>
</head>
<body>

<section class="poster">
  <div class="poster-photo" role="img" aria-label="Photo of a bright living room window with garden greenery outside, a hand wiping the glass with a squeegee"></div>
  <svg class="poster-shapes" width="1109" height="738" viewBox="0 0 1109 738" aria-hidden="true">
    <path d="M0,0 C320,10 660,160 820,400 L0,400 Z" fill="#ffffff" fill-opacity=".86"/>
    <path d="M0,372 L770,418 L770,430 L0,385 Z" fill="var(--band-edge)"/>
    <path d="M0,385 L728,428 L728,540 L0,598 Z" fill="var(--band)"/>
    <path d="M380,563 L1109,510 L1109,524 L380,576 Z" fill="var(--band-edge)"/>
    <path d="M400,576 L1109,524 L1109,712 L400,712 Z" fill="var(--band)"/>
  </svg>
  <div class="wordmark">
    <div class="wordmark-name">brisk<span class="wordmark-square"></span></div>
    <div class="wordmark-tag">window cleaning services</div>
  </div>
  <p class="band-text one">Guaranteed to make your<br>home feel new again</p>
  <p class="band-text two">Fed up with your dirty window<br>call us now : +71 5550 1290</p>
</section>

<section class="referral-front">
  <article class="card-front">
    <div class="mascot" role="img" aria-label="Blue cartoon bird mascot holding a megaphone"></div>
    <div class="pill">Refer A Friend<br>To</div>
    <div class="front-brand">brisk<span class="sq"></span></div>
    <div class="front-tag">window cleaning services</div>
    <div class="front-get">and get a</div>
    <div class="front-amount">£10</div>
    <div class="front-voucher">VOUCHER</div>
    <p class="front-thanks">as a little<br><b>thank you</b><br>from us</p>
    <div class="front-foot">see reverse for more detail</div>
  </article>
  <article class="card-front">
    <div class="mascot" role="img" aria-label="Blue cartoon bird mascot holding a megaphone"></div>
    <div class="pill">Refer A Friend<br>To</div>
    <div class="front-brand">brisk<span class="sq"></span></div>
    <div class="front-tag">window cleaning services</div>
    <div class="front-get">and get a</div>
    <div class="front-amount">£10</div>
    <div class="front-voucher">VOUCHER</div>
    <p class="front-thanks">as a little<br><b>thank you</b><br>from us</p>
    <div class="front-foot">see reverse for more detail</div>
  </article>
  <article class="card-front">
    <div class="mascot" role="img" aria-label="Blue cartoon bird mascot holding a megaphone"></div>
    <div class="pill">Refer A Friend<br>To</div>
    <div class="front-brand">brisk<span class="sq"></span></div>
    <div class="front-tag">window cleaning services</div>
    <div class="front-get">and get a</div>
    <div class="front-amount">£10</div>
    <div class="front-voucher">VOUCHER</div>
    <p class="front-thanks">as a little<br><b>thank you</b><br>from us</p>
    <div class="front-foot">see reverse for more detail</div>
  </article>
</section>

<section class="referral-back">
  <article class="card-back">
    <span class="hang-hole"></span>
    <div class="back-brand">brisk<span class="sq"></span></div>
    <div class="back-title">Your Details:</div>
    <div class="field">Name:</div>
    <div class="field gap">Address:</div>
    <div class="field line"></div>
    <div class="sub">Your Friend’s Details:</div>
    <div class="field gap">Name:</div>
    <div class="field gap">Address:</div>
    <div class="field line"></div>
    <div class="field">Telephone No:</div>
    <p class="terms">You will receive a £10 voucher redeemable against any of our services, on completion of your friend’s first clean. Must be within the areas we cover. You will receive a voucher for each referral. Recommend us to as many friends as you can! Thank you for your loyal support</p>
  </article>
  <article class="card-back">
    <span class="hang-hole"></span>
    <div class="back-brand">brisk<span class="sq"></span></div>
    <div class="back-title">Your Details:</div>
    <div class="field">Name:</div>
    <div class="field gap">Address:</div>
    <div class="field line"></div>
    <div class="sub">Your Friend’s Details:</div>
    <div class="field gap">Name:</div>
    <div class="field gap">Address:</div>
    <div class="field line"></div>
    <div class="field">Telephone No:</div>
    <p class="terms">You will receive a £10 voucher redeemable against any of our services, on completion of your friend’s first clean. Must be within the areas we cover. You will receive a voucher for each referral. Recommend us to as many friends as you can! Thank you for your loyal support</p>
  </article>
  <article class="card-back">
    <span class="hang-hole"></span>
    <div class="back-brand">brisk<span class="sq"></span></div>
    <div class="back-title">Your Details:</div>
    <div class="field">Name:</div>
    <div class="field gap">Address:</div>
    <div class="field line"></div>
    <div class="sub">Your Friend’s Details:</div>
    <div class="field gap">Name:</div>
    <div class="field gap">Address:</div>
    <div class="field line"></div>
    <div class="field">Telephone No:</div>
    <p class="terms">You will receive a £10 voucher redeemable against any of our services, on completion of your friend’s first clean. Must be within the areas we cover. You will receive a voucher for each referral. Recommend us to as many friends as you can! Thank you for your loyal support</p>
  </article>
</section>

</body>
</html>
```